A colorful, playful, nerdy, creative logo for a business analytics and marketing analytics company.

We need a logo and website design for a new company based in Florida called Pathways Above Numbers Guild. We provide marketing, consumer and business insights through the use of market research, business analytics and marketing analytics. We are a collection of several individuals each with specific expertise and come together to provide the best possible insights about their consumers/guests/customers. We would like to see a design that uses colors that show a free spirit but deeply rooted in analytics " a super nerd " Along those steps, we would like to see either a playful, nerdy, creative logo or one that includes the full or partial name of the company. We have simplified our "brand" by saying when you initially start with us you may have several questions "?" through the process of learning about your consumers/brand ">" incredible solutions, strategies are developed "!" So something like a ?>! symbol would be interesting. Although the name of the company sounds very complex and very long to write, we would be interested in thoughtful ways of shorting the name or incorporating into the final logo design
Updates

Target Market(s)

Business or organizations that currently do not have an analytics/research function

Industry/Entity Type

Business

Contact Information for Business Card

Incorporate final logo and colors font. In the past, I have used a "wordle" website to show 10 common research terms scattered about .. showing them as strength or core competencies.

Logo Text

?>! or Pathways Above Numbers Guild or PAN Guild

Coding

Coded - Design and coding required

Number of Pages Required

4 page

Font styles to use
Sans Serif
Decorative

Requirements
Must have
• The project must communicate analytics/scientific. It must we unique but not unique for the sack of being unique.
• It must either be a logo or a simple way to communicate the company name Pathways Above Numbers Guild
Nice to have
• Again incorporating the symbols ?>! in that order. Showing confusion to gaining insights and then developing incredible solutions that are used to effect consumer behavior.
• Look to CPG ( consumer package goods) industry to input
Should not have
• I am pretty open to suggestions.

```html
<!DOCTYPE html>
<html lang="en">
<head>
<meta charset="utf-8">
<title>Pathways Above Numbers Guild</title>
<link href="https://fonts.googleapis.com/css2?family=Cabin:wght@400;500;600&family=Open+Sans:wght@400;600;700&display=swap" rel="stylesheet">
<style>
:root{
  --red:#d6232b;
  --red-deep:#a9121a;
  --red-dark:#7d0c11;
  --ink:#3a3a3a;
  --grey:#777;
  --line:#e6e6e6;
  --white:#fff;
  --photo-grey:#c9c9c9;
}
*{box-sizing:border-box;margin:0;padding:0}
html,body{width:1200px;height:4193px;overflow:hidden}
body{font-family:"Open Sans",Arial,sans-serif;color:var(--ink);background:var(--white);position:relative}
section,header,footer{position:absolute;left:0;width:1200px;overflow:hidden}
.abs{position:absolute}
h1,h2,h3,.head{font-family:"Cabin",Arial,sans-serif;font-weight:400}
.btn{position:absolute;display:block;height:28px;border:1.5px solid var(--red);border-radius:14px;color:var(--red);font:700 10px "Open Sans",sans-serif;letter-spacing:2px;text-align:center;line-height:25px;text-transform:uppercase;background:var(--white)}
.btn.light{border-color:var(--white);color:var(--white);background:transparent}

/* header / hero */
.hero{top:0;height:560px;background:linear-gradient(100deg,#cfc7c0 0%,#a49a92 30%,#6e5a4c 55%,#3d3029 80%,#5b4c40 100%)}
.hero-photo{position:absolute;inset:0}
.topbar{position:absolute;top:14px;left:0;width:1200px;height:36px}
.brand{position:absolute;left:18px;top:4px;display:flex;align-items:center;gap:8px;color:var(--white);font:600 15px "Cabin",sans-serif}
.brand-dot{width:22px;height:22px;border-radius:50%;background:#f29a1f}
.nav{position:absolute;left:386px;top:10px;display:flex;gap:24px;font-size:11px;color:var(--white)}
.mail{position:absolute;left:920px;top:10px;font-size:11px;color:#ff4b52}
.socials{position:absolute;left:1030px;top:10px;display:flex;gap:12px}
.socials span{width:12px;height:12px;border-radius:50%;background:var(--white)}
.search{position:absolute;left:1133px;top:8px}
.lang{position:absolute;left:1160px;top:7px;width:20px;height:20px;border-radius:50%;background:var(--red)}
.slide-circle{position:absolute;left:559px;top:112px;width:364px;height:364px;border-radius:50%;background:rgba(214,35,43,.95);color:var(--white);text-align:center}
.slide-circle h1{font-size:34px;margin-top:62px}
.slide-circle p{font-size:11px;line-height:17px;width:262px;margin:12px auto 0}
.slide-badge{position:absolute;left:582px;top:390px;width:100px;height:100px;border-radius:50%;background:var(--white);display:flex;align-items:center;justify-content:center}
.arrow{position:absolute;top:303px;width:20px;height:20px;border-radius:50%;background:var(--red)}

/* welcome */
.welcome{top:560px;height:307px;text-align:center}
.welcome h2{color:var(--red);font-size:28px;margin-top:45px}
.welcome p{width:580px;margin:16px auto 0;font-size:11px;line-height:17px;color:var(--grey)}
.welcome p+p{margin-top:12px}

/* insights */
.insights{top:867px;height:363px;background:linear-gradient(#f7f7f7,#fff 40%)}
.insights h2{text-align:center;color:var(--red);font-size:28px;line-height:34px;margin-top:42px}
.panels{position:absolute;top:133px;left:0;display:flex}
.panel{position:relative;width:400px;height:230px;color:var(--white)}
.panel:nth-child(1){background:linear-gradient(120deg,#c81a22,#e0262e 60%,#b8141b)}
.panel:nth-child(2){background:linear-gradient(120deg,#d4222a,#a91218 70%,#c71c24)}
.panel:nth-child(3){background:linear-gradient(120deg,#8f0d13,#d6232b 40%,#c01a21)}
.panel h3{position:absolute;left:16px;top:82px;font-size:24px}
.panel:nth-child(2) h3,.panel:nth-child(2) p,.panel:nth-child(2) .btn{left:28px}
.panel:nth-child(3) h3,.panel:nth-child(3) p,.panel:nth-child(3) .btn{left:28px}
.panel p{position:absolute;left:16px;top:114px;width:275px;font-size:10px;line-height:13px}
.panel .btn{top:178px;left:16px;width:136px}

/* experts */
.experts{top:1230px;height:840px;background:linear-gradient(90deg,#d2d2d2 0%,#bdbdbd 20%,#ececec 45%,#f6f6f6 70%,#e3e3e3 100%)}
.experts h2{text-align:center;color:var(--red);font-size:28px;margin-top:48px}
.expert{position:absolute;width:240px;text-align:center}
.avatar{width:152px;height:152px;border-radius:50%;border:3px solid var(--red);margin:0 auto;padding:6px;background:var(--white)}
.avatar div{width:100%;height:100%;border-radius:50%;background:linear-gradient(#b9aea6,#7e726b)}
.expert h3{color:var(--red);font-size:18px;font-weight:500;margin-top:14px}
.expert p{font-size:10px;line-height:14px;color:var(--grey);margin:14px auto 0;width:200px}
.experts .btn{left:532px;top:770px;width:136px}

/* quote */
.quote{top:2070px;height:308px;background:linear-gradient(90deg,#cf1f27 0%,#d6232b 55%,#9a1016 75%,#2a2a2a 100%);text-align:center;color:var(--white)}
.quote-mark{position:absolute;left:568px;top:48px;width:60px;height:60px;border-radius:50%;background:var(--white);border:3px solid var(--red-deep);display:flex;align-items:center;justify-content:center;color:var(--red);font:700 38px Georgia,serif;line-height:1}
.quote blockquote{position:absolute;left:330px;top:144px;width:540px;font:700 15px/24px "Open Sans",sans-serif}
.quote cite{position:absolute;left:0;width:1200px;top:202px;font-style:normal;font-size:12px;opacity:.85}

/* products */
.products{top:2378px;height:657px;background:linear-gradient(90deg,#bcbcbc,#ededed 30%,#f2f2f2 70%,#c4c4c4)}
.products h2{text-align:center;color:var(--red);font-size:26px;margin-top:48px}
.tile{position:absolute;width:344px;height:200px;background:var(--red);color:var(--white);text-align:center}
.tile .icon{margin-top:48px}
.tile h3{font-size:24px;margin-top:14px}
.tile.text{background:var(--white);color:var(--grey);text-align:center}
.tile.text h3{color:var(--red);margin-top:28px;font-size:24px}
.tile.text p{font-size:10px;line-height:14px;width:290px;margin:10px auto 0}

/* news */
.news{top:3035px;height:811px;background:linear-gradient(90deg,#8e0c12,#d6232b 25%,#d9262e 75%,#8c0b11)}
.news h2{text-align:center;color:var(--white);font-size:26px;margin-top:46px}
.cats{position:absolute;left:249px;top:134px;width:204px;color:var(--white)}
.cats h4{font:600 14px "Cabin",sans-serif;margin-bottom:10px;display:flex;align-items:center;gap:6px}
.cats li{list-style:none;height:38px;line-height:37px;border-bottom:1px solid rgba(255,255,255,.35);font-size:10px;font-weight:600;padding-left:22px;position:relative}
.cats li::before{content:"";position:absolute;left:10px;top:17px;width:3px;height:3px;border-radius:50%;background:currentColor}
.cats li.active{background:var(--white);color:var(--red)}
.card{position:absolute;width:227px;color:var(--white)}
.card .thumb{height:108px;background:linear-gradient(#e9e9ef,#8e93a8)}
.card h4{font-size:9px;font-weight:700;margin-top:14px;line-height:12px}
.card p{font-size:9px;line-height:13px;margin-top:8px}
.card .more{font-size:9px;font-weight:700;margin-top:8px;display:block}

/* newsletter */
.newsletter{top:3846px;height:294px;text-align:center}
.newsletter h2{color:var(--red);font-size:38px;margin-top:45px}
.field{position:absolute;top:131px;width:219px;height:36px;border:1px solid #d8aeb0;font-size:10px;color:var(--grey);text-align:left;padding:11px 8px}
.newsletter .btn{left:532px;top:222px;width:136px}

footer{top:4140px;height:53px;background:var(--red-dark);color:var(--white);font-size:10px}
footer .copy{position:absolute;left:249px;top:20px}
footer .socials{left:558px;top:20px;gap:14px}
footer .socials span{width:10px;height:10px}
</style>
</head>
<body>
<svg width="0" height="0" style="position:absolute" aria-hidden="true">
  <symbol id="chart" viewBox="0 0 60 44">
    <path d="M4 2v38h54" fill="none" stroke="currentColor" stroke-width="3"/>
    <rect x="11" y="28" width="6" height="10" fill="currentColor"/>
    <rect x="21" y="22" width="6" height="16" fill="currentColor"/>
    <rect x="31" y="25" width="6" height="13" fill="currentColor"/>
    <rect x="41" y="16" width="6" height="22" fill="currentColor"/>
    <path d="M10 22l12-10 9 6 16-13" fill="none" stroke="currentColor" stroke-width="2.5"/>
    <path d="M42 4h7v7" fill="none" stroke="currentColor" stroke-width="2.5"/>
  </symbol>
</svg>

<header class="hero">
  <div class="hero-photo" role="img" aria-label="Photo of a smiling businessman in a bright office, colleagues blurred behind him"></div>
  <div class="topbar">
    <div class="brand"><span class="brand-dot"></span>Pathways Above Numbers Guild</div>
    <nav class="nav"><span>Business Intelligence</span><span>Solutions</span><span>Products</span><span>Services</span><span>Support</span><span>Company</span></nav>
    <span class="mail">hello@panguild.com</span>
    <div class="socials"><span></span><span></span><span></span><span></span></div>
    <svg class="search" width="14" height="14" viewBox="0 0 14 14"><circle cx="6" cy="6" r="4.5" fill="none" stroke="#fff" stroke-width="1.6"/><path d="M9.5 9.5l3.5 3.5" stroke="#fff" stroke-width="1.8"/></svg>
    <span class="lang"></span>
  </div>
  <span class="arrow" style="left:247px"></span>
  <span class="arrow" style="left:933px"></span>
  <div class="slide-circle">
    <h1>Thinking Faster</h1>
    <p>Lorem Ipsum has been the industry's standard dummy text ever since the 1500s, when an unknown printer took a galley of type and scrambled it to make a type specimen book. It has survived not only five centuries, but also the leap into electronic typesetting, remaining essentially unchanged.</p>
    <p>Lorem Ipsum is simply dummy text of the printing and typesetting industry.</p>
  </div>
  <div class="slide-badge"><svg width="56" height="42" style="color:var(--red)"><use href="#chart"/></svg></div>
</header>

<section class="welcome">
  <h2>Welcome to Pathways Above Numbers Guild</h2>
  <p>Lorem Ipsum has been the industry's standard dummy text ever since the 1500s, when an unknown printer took a galley of type and scrambled it to make a type specimen book.</p>
  <p>Lorem Ipsum has been the industry's standard dummy text ever since the 1500s, when an unknown printer took a galley of type and scrambled it to make a type specimen book. It has survived not only five centuries, but also the leap into electronic typesetting, remaining essentially unchanged.</p>
  <a class="btn" style="left:532px;top:240px;width:136px">Learn More</a>
</section>

<section class="insights">
  <h2>We Provide Marketing, Consumer and<br>Business Insights Through:</h2>
  <div class="panels">
    <div class="panel" role="img" aria-label="Red-tinted photo of people working with data">
      <h3>Market Research</h3>
      <p>Lorem Ipsum has been the industry's standard dummy text ever since the 1500s, when an unknown printer took a galley of type and scrambled it to make a type specimen book.</p>
      <a class="btn light">Learn More</a>
    </div>
    <div class="panel" role="img" aria-label="Red-tinted photo of an analytics dashboard">
      <h3>Business Analytics</h3>
      <p>Lorem Ipsum has been the industry's standard dummy text ever since the 1500s, when an unknown printer took a galley of type and scrambled it to make a type specimen book.</p>
      <a class="btn light">Learn More</a>
    </div>
    <div class="panel" role="img" aria-label="Red-tinted photo of a marketing meeting">
      <h3>Marketing Analytics</h3>
      <p>Lorem Ipsum has been the industry's standard dummy text ever since the 1500s, when an unknown printer took a galley of type and scrambled it to make a type specimen book.</p>
      <a class="btn light">Learn More</a>
    </div>
  </div>
</section>

<section class="experts" role="img" aria-label="Faded greyscale photo of businessmen in suits behind the experts">
  <h2>Our Experts</h2>
  <div class="expert" style="left:481px;top:126px">
    <div class="avatar"><div role="img" aria-label="Portrait of the deep learning expert"></div></div>
    <h3>Deep learning</h3>
    <p>Lorem Ipsum has been the industry's standard dummy text ever since the 1500s, when an</p>
  </div>
  <div class="expert" style="left:218px;top:294px">
    <div class="avatar"><div role="img" aria-label="Portrait of the evolutionary computing expert"></div></div>
    <h3>Evolutionary Computing</h3>
    <p>Lorem Ipsum has been the industry's standard dummy text ever since the 1500s, when an</p>
  </div>
  <div class="expert" style="left:741px;top:294px">
    <div class="avatar"><div role="img" aria-label="Portrait of the graph analytics expert"></div></div>
    <h3>Graph Analytics</h3>
    <p>Lorem Ipsum has been the industry's standard dummy text ever since the 1500s, when an</p>
  </div>
  <div class="expert" style="left:481px;top:462px">
    <div class="avatar"><div role="img" aria-label="Portrait of the machine learning expert"></div></div>
    <h3>Machine learning</h3>
    <p>Lorem Ipsum has been the industry's standard dummy text ever since the 1500s, when an</p>
  </div>
  <a class="btn">More Experts</a>
</section>

<section class="quote" role="img" aria-label="Red-tinted photo of a laptop on a desk">
  <div class="quote-mark">&ldquo;</div>
  <blockquote>Lorem Ipsum has been the industry's standard dummy text ever since the 1500s, when an unknown printer took a galley of type and</blockquote>
  <cite>Mara Lindqvist</cite>
</section>

<section class="products" role="img" aria-label="Faded greyscale photo of a business team at a table">
  <h2>Products</h2>
  <div class="tile" style="left:249px;top:122px"><svg class="icon" width="60" height="44" style="color:#fff"><use href="#chart"/></svg><h3>Short Feature List</h3></div>
  <div class="tile text" style="left:607px;top:122px">
    <h3>The Keel Suite</h3>
    <p>Lorem Ipsum has been the industry's standard dummy text ever since the 1500s, when an unknown printer took a galley of type and scrambled it to make a type specimen book.</p>
    <p>Lorem Ipsum has been the industry's standard dummy text ever since the 1500s, when an unknown printer took a galley of type and scrambled it to make a type specimen book.</p>
  </div>
  <div class="tile" style="left:249px;top:338px"><svg class="icon" width="60" height="44" style="color:#fff"><use href="#chart"/></svg><h3>Ostrava</h3></div>
  <div class="tile" style="left:607px;top:338px"><svg class="icon" width="60" height="44" style="color:#fff"><use href="#chart"/></svg><h3>Signal-It</h3></div>
</section>

<section class="news" role="img" aria-label="Red-tinted photo of two businessmen standing at the sides">
  <h2>News Section</h2>
  <div class="cats">
    <h4><svg width="12" height="12" viewBox="0 0 12 12"><path d="M1 1h4v4H1zM7 1h4v4H7zM1 7h4v4H1zM7 7h4v4H7z" fill="#fff"/></svg>Categories</h4>
    <ul>
      <li class="active">simply dummy text of the printing</li>
      <li>It is a long established</li>
      <li>The point of</li>
      <li>Many desktop publishing</li>
      <li>simply dummy text of the printing</li>
      <li>The point of</li>
      <li>Many desktop publishing</li>
      <li>Many desktop publishing</li>
      <li>simply dummy text of the printing</li>
      <li>The point of</li>
      <li>Many desktop publishing</li>
      <li>simply dummy text of the printing</li>
      <li>The point of</li>
      <li>Many desktop publishing</li>
    </ul>
  </div>
  <article class="card" style="left:478px;top:125px">
    <div class="thumb" role="img" aria-label="Photo of a team meeting around a table"></div>
    <h4>Construction Consulting<br>Project Builders</h4>
    <p>Lorem Ipsum has been the industry's standard dummy text ever since the 1500s, when an unknown printer took a galley of type and scrambled it to make a type specimen book. It has survived not only five centuries, but also the leap into electronic typesetting.</p>
    <span class="more">Read More</span>
  </article>
  <article class="card" style="left:724px;top:125px">
    <div class="thumb" role="img" aria-label="Photo of colleagues discussing at a laptop"></div>
    <h4>Construction Consulting<br>Project Builders</h4>
    <p>Lorem Ipsum has been the industry's standard dummy text ever since the 1500s, when an unknown printer took a galley of type and scrambled it to make a type specimen book. It has survived not only five centuries, but also the leap into electronic typesetting.</p>
    <span class="more">Read More</span>
  </article>
  <article class="card" style="left:478px;top:405px">
    <div class="thumb" role="img" aria-label="Photo of a small group in conversation"></div>
    <h4>Construction Consulting<br>Project Builders</h4>
    <p>Lorem Ipsum has been the industry's standard dummy text ever since the 1500s, when an unknown printer took a galley of type and scrambled it to make a type specimen book. It has survived not only five centuries, but also the leap into electronic typesetting.</p>
    <span class="more">Read More</span>
  </article>
  <article class="card" style="left:724px;top:405px">
    <div class="thumb" role="img" aria-label="Photo of people working at computer screens"></div>
    <h4>Construction Consulting<br>Project Builders</h4>
    <p>Lorem Ipsum has been the industry's standard dummy text ever since the 1500s, when an unknown printer took a galley of type and scrambled it to make a type specimen book. It has survived not only five centuries, but also the leap into electronic typesetting.</p>
    <span class="more">Read More</span>
  </article>
</section>

<section class="newsletter">
  <h2>Newsletter</h2>
  <div class="field" style="left:249px">First Name</div>
  <div class="field" style="left:489px">Last Name</div>
  <div class="field" style="left:730px">Email</div>
  <a class="btn">Submit</a>
</section>

<footer>
  <span class="copy">© Copyright Pathways Above Numbers Guild</span>
  <div class="socials"><span></span><span></span><span></span><span></span></div>
</footer>
</body>
</html>
```